harbor mental health stationary

Please help turn this logo into a total image for my business.
Stationary need to be able to be individualized for each mental health practitioners

Some generic info about services
Clinical Psychology - Consultant Psychiatry - Locum Services - Medico-legal - Architectural Adviser Clinical and Medical Facilities

Target Market(s)

Letter head for doctors, courts, patients.

Industry/Entity Type

Mental Health

Requirements
Must have
• area where practitioners details can be listed and logo on page
Nice to have
• embossed section

```html
<!DOCTYPE html>
<html lang="en">
<head>
<meta charset="utf-8">
<title>Harbor Mental Health — Letterhead</title>
<link rel="stylesheet" href="https://fonts.googleapis.com/css2?family=Fira+Sans:wght@300;400;500;700&display=swap">
<style>
  :root {
    --navy: #163a60;
    --ocean: #2472a8;
    --ink: #1c1c1c;
    --text-soft: #3a3a3a;
    --sidebar-text: #eaf2f9;
    --footer-bg: #e4e6e9;
    --page: #ffffff;
    --brand: #2f6a96;
  }
  * { margin: 0; padding: 0; box-sizing: border-box; }
  html, body { width: 901px; height: 1200px; overflow: hidden; background: #f0f0f0; }
  body { font-family: "Fira Sans", Arial, sans-serif; color: var(--ink); }

  .letterhead {
    position: relative;
    width: 901px; height: 1200px;
    background: var(--page);
    overflow: hidden;
  }

  /* Sidebar */
  .services {
    position: absolute; left: 0; top: 0;
    width: 239px; height: 1200px;
    background: linear-gradient(180deg, var(--navy) 0%, #1b5585 55%, var(--ocean) 100%);
    color: var(--sidebar-text);
    font-weight: 300;
  }
  .services > * { position: absolute; left: 27px; right: 12px; }
  .services .lead { top: 33px; font-size: 13.5px; line-height: 16px; }
  .services .lead strong { display: block; font-size: 16.5px; font-weight: 500; line-height: 20px; margin-top: 4px; }
  .services .intro { top: 112px; font-size: 13.5px; line-height: 16.5px; }
  .services ul { list-style: none; font-size: 15px; }
  .services li::before { content: "• "; }
  .services .conditions { top: 219px; line-height: 22.9px; }
  .services .clients-title { top: 543px; font-size: 15px; font-weight: 300; line-height: 20px; }
  .services .clients { top: 624px; line-height: 20.5px; }
  .services .other { top: 828px; font-size: 15px; font-weight: 300; line-height: 20px; }
  .services .extras { top: 870px; line-height: 20.5px; }
  .rebate { top: 1100px; }
  .rebate .title { font-size: 17px; font-weight: 500; line-height: 22px; white-space: nowrap; }
  .rebate .sub { font-size: 13px; line-height: 19px; letter-spacing: 0.4px; margin-top: 3px; }

  /* Header */
  .trading {
    position: absolute; left: 264px; top: 22px;
    font-size: 12.5px; color: var(--ink);
  }
  .brand {
    position: absolute; left: 264px; top: 56px;
    display: flex; align-items: center; gap: 14px;
  }
  .brand .mark { width: 48px; height: 48px; background: var(--brand); }
  .brand .name {
    font-size: 30px; font-weight: 400; color: var(--brand);
    letter-spacing: 0.5px; line-height: 1;
  }
  .practitioner { position: absolute; left: 264px; top: 126px; }
  .practitioner .person { font-size: 17px; font-weight: 700; }
  .practitioner p { font-size: 12.5px; line-height: 16px; color: var(--text-soft); }
  .practitioner .person + p { margin-top: 3px; }

  /* Footer contact */
  .contact {
    position: absolute; left: 502px; top: 1054px;
    width: 399px; height: 146px;
    background: var(--footer-bg);
    padding: 26px 20px 0 0;
    text-align: right;
    font-size: 15px; line-height: 22px; color: var(--ink);
  }
  .contact b { font-weight: 700; }
  .contact .gap { margin-left: 16px; }
</style>
</head>
<body>
<main class="letterhead">
  <aside class="services">
    <p class="lead">Specialising in the<br>treatment of:<strong>Depression &amp; Anxiety</strong></p>
    <p class="intro">Provider of psychological<br>assessment and<br>therapy for other<br>mental health problems<br>including:</p>
    <ul class="conditions">
      <li>Phobias</li>
      <li>Panic</li>
      <li>Adjustment disorder</li>
      <li>Bereavement</li>
      <li>Post-traumatic<br>stress disorder</li>
      <li>Eating disorders</li>
      <li>Obsessive Compulsive<br>disorder</li>
      <li>Bipolar disorder</li>
      <li>Schizophrenia</li>
      <li>Sleep problems</li>
      <li>Personality issues</li>
    </ul>
    <h3 class="clients-title">Counselling and<br>therapy<br>provided for:</h3>
    <ul class="clients">
      <li>Families</li>
      <li>Couples (Couples<br>Connect Program)</li>
      <li>Group</li>
      <li>Individuals</li>
      <li>Children</li>
      <li>Adolescents</li>
      <li>Adults</li>
      <li>Older persons</li>
    </ul>
    <h3 class="other">Other Services:</h3>
    <ul class="extras">
      <li>Cognitive Assessment</li>
      <li>Neuropsychological<br>Assessment</li>
      <li>Memory &amp; Dementia<br>Screening</li>
      <li>Employee Assistance<br>Program</li>
      <li>Stress Management</li>
      <li>Medicolegal reports</li>
    </ul>
    <div class="rebate">
      <p class="title">HEALTH FUND REBATE:</p>
      <p class="sub">SPECIALIST CLINICAL<br>PSYCHOLOGIST RATE</p>
    </div>
  </aside>

  <p class="trading">Harbor Mental Health Services Pty Ltd as Trustee for M &amp; D Hollis Family Trust trading as</p>

  <div class="brand">
    <span class="mark"></span>
    <span class="name">Harbor Mental Health</span>
  </div>

  <section class="practitioner">
    <h2 class="person">Maren Hollis</h2>
    <p>M. Psych (Clinical), M. Genetic Couns., B.A. (Psych),</p>
    <p>Reg. no: PSY0000418273 Provider no: 5830264T</p>
    <p>Member of the National Psychological Society</p>
  </section>

  <footer class="contact">
    <p><b>Phone</b>: (08) 9312 4480 or 0491 562 207</p>
    <p><b>Address</b>: 24 Wexcombe Place, KELMORE 6021</p>
    <p><b>Email</b>: mhollis@hmh.net.au</p>
    <p><b>ABN</b>: 48 216 905 371<span class="gap"><b>ACN</b>: 2614 70938</span></p>
  </footer>
</main>
</body>
</html>
```